Harwick Market
Your Authentic Market Experience
Project: Harwick Market
Harwick Market - Events
Creative Brief
Bright & Fun-filled
we will not be putting a name on the card
we will not be putting an address on the card
harwickmarketmanager@plovenmail.com
www.harwickfarmersmarket-example.com
Saturdays 2pm-4pm May long weekend - September long weekend
We haven't got a specific idea for the back of the card. We just know that we like the look of double sided cards
QJMDesignworks QJMDesignworks
DorvalTownStalls DorvalTownStalls

```html
<!DOCTYPE html>
<html lang="en">
<head>
<meta charset="utf-8">
<title>Harwick Market – Stationery</title>
<link href="https://fonts.googleapis.com/css2?family=Fredoka:wght@600&family=Montserrat:wght@500;700&family=Open+Sans:wght@400;600&family=Dancing+Script:wght@600&display=swap" rel="stylesheet">
<style>
  :root {
    --bg: #eeeeee;
    --paper: #ffffff;
    --green-dark: #6f8f24;
    --green: #86a83a;
    --green-light: #b3ca6a;
    --green-pale: #e3ebcb;
    --ink: #4a4a4a;
    --ink-soft: #8a8a8a;
  }
  * { margin: 0; padding: 0; box-sizing: border-box; }
  html, body { width: 1200px; height: 799px; overflow: hidden; }
  body {
    position: relative;
    background: var(--bg);
    font-family: "Open Sans", Arial, sans-serif;
    color: var(--ink);
  }
  .piece { position: absolute; background: var(--paper); overflow: hidden; }

  .brand {
    display: flex; align-items: center; gap: 6px;
    font-family: "Fredoka", "Arial Rounded MT Bold", sans-serif;
    font-weight: 600; color: var(--green-dark); line-height: 1;
  }
  .brand-dot { border-radius: 50%; background: var(--green); flex: none; }

  .contact { font-family: "Montserrat", Arial, sans-serif; color: var(--ink); }
  .contact .phone { display: flex; align-items: center; gap: 5px; font-weight: 700; }
  .contact .line { color: var(--ink-soft); font-weight: 500; }
  .phone-icon { flex: none; }

  .art { position: absolute; }

  /* Letterhead */
  .letterhead { left: 89px; top: 113px; width: 444px; height: 619px; }
  .letterhead .brand { position: absolute; left: 32px; top: 44px; font-size: 20px; }
  .letterhead .brand-dot { width: 14px; height: 14px; }
  .letterhead .contact { position: absolute; left: 270px; top: 38px; font-size: 11px; }
  .letterhead .contact .line { font-size: 6.5px; margin-top: 3px; padding-left: 17px; }
  .letter-date { position: absolute; right: 30px; top: 118px; font-size: 6.5px; color: var(--ink-soft); }
  .letter-body { position: absolute; left: 32px; top: 148px; width: 360px; font-size: 6.8px; line-height: 1.7; color: var(--ink-soft); }
  .letter-body p { margin-bottom: 10px; }
  .letter-body .salutation { color: var(--ink); margin-bottom: 12px; }
  .letter-sign { position: absolute; left: 32px; top: 458px; font-size: 6.8px; line-height: 1.7; color: var(--ink-soft); }
  .letter-sign .name { margin-top: 18px; color: var(--ink); }
  .letterhead .art { left: 140px; bottom: 0; width: 304px; height: 130px;
    background: linear-gradient(180deg, rgba(227,235,203,0) 0%, var(--green-pale) 55%, #d5e0b0 100%); }

  /* Business card front */
  .card-front { left: 569px; top: 84px; width: 290px; height: 161px; }
  .card-front .brand { position: absolute; left: 16px; top: 26px; font-size: 17px; }
  .card-front .brand-dot { width: 12px; height: 12px; }
  .card-front .tagline { position: absolute; left: 16px; top: 48px; font-size: 5.5px; color: var(--green-dark); letter-spacing: .4px; text-transform: uppercase; }
  .card-front .contact { position: absolute; left: 160px; top: 20px; font-size: 10px; }
  .card-front .contact .line { font-size: 5.5px; margin-top: 3px; padding-left: 15px; }
  .card-front .hills { position: absolute; left: 0; bottom: 0; width: 290px; height: 90px; }
  .card-front .hours { position: absolute; left: 14px; bottom: 16px; font-family: "Montserrat", Arial, sans-serif; color: #fff; font-size: 7px; font-weight: 700; display: flex; align-items: center; gap: 8px; }
  .card-front .hours small { font-size: 5.2px; font-weight: 500; line-height: 1.3; }

  /* Business card back */
  .card-back { left: 569px; top: 257px; width: 290px; height: 163px; }
  .card-back .motto { position: absolute; left: 0; top: 10px; width: 100%; text-align: center; font-family: "Dancing Script", cursive; font-size: 15px; color: var(--green-dark); }
  .card-back .art { left: 0; bottom: 0; width: 290px; height: 118px;
    background: linear-gradient(180deg, #ffffff 0%, var(--green-pale) 40%, var(--green-light) 100%); }

  /* Notebook */
  .notebook { left: 900px; top: 91px; width: 223px; height: 360px; border-radius: 18px; background: var(--green); }
  .notebook .pattern { position: absolute; inset: 0; background: linear-gradient(135deg, #7c9d31, #92b244); }
  .notebook .title { position: absolute; left: 32px; top: 108px; width: 160px; height: 92px; border-radius: 8px; background: rgba(255,255,255,.85); }
  .notebook .brand { position: absolute; left: 0; width: 100%; justify-content: center; bottom: 20px; font-size: 12px; color: #fff; }
  .notebook .brand-dot { width: 8px; height: 8px; background: #fff; }

  /* Envelope */
  .envelope { left: 576px; top: 449px; width: 547px; height: 278px; }
  .envelope .flap { position: absolute; left: 0; top: 0; width: 547px; height: 70px; }
  .envelope .contact { position: absolute; left: 22px; top: 56px; font-size: 12px; }
  .envelope .contact .line { font-size: 6px; margin-top: 3px; padding-left: 17px; }
  .envelope .brand { position: absolute; left: 300px; top: 78px; font-size: 20px; }
  .envelope .brand-dot { width: 14px; height: 14px; }
  .envelope .art { left: 0; bottom: 0; width: 547px; height: 150px;
    background: linear-gradient(180deg, rgba(227,235,203,0) 0%, var(--green-pale) 50%, #d5e0b0 100%); }
</style>
</head>
<body>

<!-- Letterhead -->
<section class="piece letterhead">
  <div class="brand"><span class="brand-dot"></span>Harwick Market</div>
  <div class="contact">
    <div class="phone">
      <svg class="phone-icon" width="12" height="12" viewBox="0 0 12 12"><circle cx="6" cy="6" r="6" fill="#86a83a"/><path d="M4 3.2l1.1 1.3-.6.8c.4.8 1 1.4 1.8 1.8l.8-.6L8.8 7.6 8.3 8.8C6 8.5 3.6 6.1 3.2 3.7z" fill="#fff"/></svg>
      555-210-3947
    </div>
    <div class="line">harwickmarketmanager@plovenmail.com</div>
    <div class="line">www.harwickfarmersmarket-example.com</div>
  </div>
  <div class="letter-date">November 1, 2021</div>
  <div class="letter-body">
    <p class="salutation">Dear Mr. Calloway,</p>
    <p>Thank you for joining us this season. Our stalls bring fresh produce, baked goods and local crafts to the heart of town every weekend. We are proud to support growers and makers who care about quality, and we hope you will visit often.</p>
    <p>Vendor applications for the coming season are now open. Please send your details along with a short description of your products, and our team will reply within one week to confirm your space.</p>
    <p>We look forward to seeing you at the market and sharing another bright, fun-filled summer together.</p>
  </div>
  <div class="letter-sign">
    <div>Sincerely yours,</div>
    <div class="name">Your Name</div>
    <div>Managing Director</div>
  </div>
  <div class="art" role="img" aria-label="Faint illustration of a farmhouse and windmill"></div>
</section>

<!-- Business card front -->
<section class="piece card-front">
  <div class="brand"><span class="brand-dot"></span>Harwick Market</div>
  <div class="tagline">Your Authentic Market Experience</div>
  <div class="contact">
    <div class="phone">
      <svg class="phone-icon" width="11" height="11" viewBox="0 0 12 12"><circle cx="6" cy="6" r="6" fill="#86a83a"/><path d="M4 3.2l1.1 1.3-.6.8c.4.8 1 1.4 1.8 1.8l.8-.6L8.8 7.6 8.3 8.8C6 8.5 3.6 6.1 3.2 3.7z" fill="#fff"/></svg>
      555-210-3947
    </div>
    <div class="line">harwickmarketmanager@plovenmail.com</div>
    <div class="line">www.harwickfarmersmarket-example.com</div>
  </div>
  <svg class="hills" viewBox="0 0 290 90" preserveAspectRatio="none">
    <path d="M0 30 C60 5 130 10 180 30 S260 40 290 20 V90 H0Z" fill="#b3ca6a"/>
    <path d="M0 45 C70 25 150 30 210 48 S270 55 290 42 V90 H0Z" fill="#6f8f24"/>
  </svg>
  <div class="hours">Saturdays 2pm-4pm<small>May long weekend -<br>September long weekend</small></div>
</section>

<!-- Business card back -->
<section class="piece card-back">
  <div class="motto">Feeding your body and your soul</div>
  <div class="art" role="img" aria-label="Illustration of a farmhouse, windmill and rolling fields"></div>
</section>

<!-- Notebook -->
<section class="piece notebook">
  <div class="pattern" role="img" aria-label="Scalloped green decorative pattern"></div>
  <div class="title" role="img" aria-label="Hand-lettered Note Book title"></div>
  <div class="brand"><span class="brand-dot"></span>Harwick Market</div>
</section>

<!-- Envelope -->
<section class="piece envelope">
  <svg class="flap" viewBox="0 0 547 70" preserveAspectRatio="none">
    <path d="M0 0 H547 V8 L273 64 L0 8Z" fill="#86a83a"/>
  </svg>
  <div class="contact">
    <div class="phone">
      <svg class="phone-icon" width="13" height="13" viewBox="0 0 12 12"><circle cx="6" cy="6" r="6" fill="#86a83a"/><path d="M4 3.2l1.1 1.3-.6.8c.4.8 1 1.4 1.8 1.8l.8-.6L8.8 7.6 8.3 8.8C6 8.5 3.6 6.1 3.2 3.7z" fill="#fff"/></svg>
      555-210-3947
    </div>
    <div class="line">harwickmarketmanager@plovenmail.com</div>
    <div class="line">www.harwickfarmersmarket-example.com</div>
  </div>
  <div class="brand"><span class="brand-dot"></span>Harwick Market</div>
  <div class="art" role="img" aria-label="Faint illustration of market buildings, grain silos and fields"></div>
</section>

</body>
</html>
```